Baby Shower Invitation for Vectored Image Provided

Corinne & Dorian's Baby Shower - Black/White/Gold Colors preferred
Please use the vectored portrait image attached. I'd like us on the lower right side of the invitation.
Can be horizontal or vertical layout.
The second image attached has the information needed for you to complete.
I don't want that style copied, it is just an example.

```html
<!DOCTYPE html>
<html lang="en">
<head>
<meta charset="utf-8">
<title>Corinne Hallowell Baby Shower Invitation</title>
<link rel="stylesheet" href="https://fonts.googleapis.com/css2?family=Bebas+Neue&family=Italianno&family=Pacifico&family=Roboto:wght@400&display=swap">
<style>
  :root {
    --backdrop: #858585;
    --gold: #cfa670;
    --gold-light: #f3dfa8;
    --gold-pale: #fbf3dc;
    --cream: #fffdf8;
    --ink: #2b2b2b;
    --ink-soft: #555555;
    --portrait-dark: #2a2a2a;
    --portrait-mid: #6b5646;
  }
  * { margin: 0; padding: 0; box-sizing: border-box; }
  html, body { width: 863px; height: 1200px; overflow: hidden; background: var(--backdrop); }
  .invitation {
    position: absolute; left: 37px; top: 38px; width: 790px; height: 1124px;
    background: #ffffff; overflow: hidden;
  }
  .damask-field {
    position: absolute; inset: 0;
    background: radial-gradient(ellipse at 40% 40%, var(--gold-pale) 0%, var(--gold-light) 55%, var(--gold) 100%);
  }
  .content-panel {
    position: absolute; left: 92px; top: 127px; width: 605px; height: 870px;
    background: var(--cream);
    box-shadow: 0 0 18px 6px rgba(255,250,235,0.9);
  }
  .gold-frame {
    position: absolute; left: 16px; top: 18px; width: 574px; height: 834px;
    border: 5px solid var(--gold);
  }
  .line { position: absolute; left: 0; width: 605px; text-align: center; white-space: nowrap; }
  .headline-script { top: 52px; font-family: "Italianno", cursive; font-size: 96px; line-height: 1; color: var(--gold); }
  .headline-caps { font-family: "Bebas Neue", sans-serif; font-size: 52px; line-height: 1; color: var(--gold); }
  .caps-1 { top: 168px; }
  .caps-2 { top: 210px; }
  .body-text { font-family: "Roboto", sans-serif; font-size: 27px; line-height: 1; color: var(--ink); }
  .join-1 { top: 285px; }
  .join-2 { top: 325px; }
  .honoree { top: 372px; font-family: "Pacifico", cursive; font-size: 38px; line-height: 1.3; color: var(--gold); }
  .details {
    position: absolute; left: 67px; top: 455px; width: 472px; height: 156px;
    border-top: 2px dotted var(--ink-soft); border-bottom: 2px dotted var(--ink-soft);
  }
  .date-block {
    position: absolute; left: 0; top: 0; width: 252px; height: 100%;
    border-right: 2px dotted var(--ink-soft);
    font-family: "Bebas Neue", sans-serif; color: var(--gold); text-align: center;
  }
  .date-day { position: absolute; left: 0; width: 250px; top: 12px; font-size: 68px; line-height: 1; }
  .date-num { position: absolute; left: 0; width: 250px; top: 82px; font-size: 68px; line-height: 1; }
  .date-num sup { font-size: 32px; vertical-align: top; position: relative; top: 6px; }
  .time-venue { position: absolute; left: 252px; top: 0; width: 220px; font-family: "Roboto", sans-serif; font-size: 24px; color: var(--ink-soft); }
  .time { padding: 10px 0 0 18px; height: 46px; border-bottom: 2px dotted var(--ink-soft); }
  .venue { padding: 6px 0 0 18px; line-height: 33px; }
  .rsvp-1 { top: 632px; color: var(--ink-soft); }
  .rsvp-2 { top: 672px; color: var(--ink-soft); }
  .registry { font-family: "Pacifico", cursive; font-size: 24px; line-height: 1.4; color: var(--gold); }
  .registry-1 { top: 700px; left: -40px; }
  .registry-2 { top: 752px; left: -40px; }
  .couple-portrait {
    position: absolute; left: 519px; top: 794px; width: 251px; height: 330px;
    background: linear-gradient(180deg, var(--portrait-mid) 0%, var(--portrait-dark) 45%, var(--portrait-dark) 100%);
    border-radius: 90px 90px 0 0;
  }
</style>
</head>
<body>
  <main class="invitation">
    <div class="damask-field" role="img" aria-label="Gold and cream damask flourish pattern background"></div>
    <section class="content-panel">
      <div class="gold-frame"></div>
      <h1 class="line headline-script">Oh Boy !</h1>
      <p class="line headline-caps caps-1">A Little Man</p>
      <p class="line headline-caps caps-2">Is On The Way!</p>
      <p class="line body-text join-1">Please join us for a</p>
      <p class="line body-text join-2">Baby Shower honoring</p>
      <h2 class="line honoree">Corinne Hallowell</h2>
      <div class="details">
        <div class="date-block">
          <div class="date-day">Saturday</div>
          <div class="date-num">1<sup>st</sup> Sept</div>
        </div>
        <div class="time-venue">
          <div class="time">11:30am-2:30pm</div>
          <div class="venue">The Fernwood<br>1842 Calder St.<br>Raleigh, NC</div>
        </div>
      </div>
      <p class="line body-text rsvp-1">RSVP to Dorian at 919-555-0148</p>
      <p class="line body-text rsvp-2">by August 20th</p>
      <p class="line registry registry-1">Corinne is registered at</p>
      <p class="line registry registry-2">Little Nest Baby</p>
    </section>
    <div class="couple-portrait" role="img" aria-label="Illustrated portrait of the expecting couple standing together"></div>
  </main>
</body>
</html>
```